Business card design for event company

need design double sided in square shape ( approx 6x6cm) in matt grey shades
front side :
logo ( could be in one color like picture attached ) printpress effect in a rect box

back side :
name in big font with silver foil finish ( similar to attached pic )

phone number i would like to see how it will look like if embossed ( like in credit cards )

Sample for contact on card ( will need 5 different contacts) - pls. include small icons next to each contact

KARIM SALEHI
Managing Director

+971 50 374 6619
karim@novlinkuae.com
www.novlink.ae
Building C2 , Office 318
Marsa Tirel Park

Please consider this is an urgent project . thank you in advance

```html
<!DOCTYPE html>
<html lang="en">
<head>
<meta charset="utf-8">
<title>Novlink Business Card</title>
<link href="https://fonts.googleapis.com/css2?family=Roboto:wght@300;400;500;700&display=swap" rel="stylesheet">
<style>
  :root {
    --backdrop: #1c1c1c;
    --card-grey: #b9aea8;
    --ink-grey: #7b8087;
    --rule-grey: #8d8d90;
    --brand-orange: #dc790d;
    --logo-grey: #b2aba7;
  }
  * { margin: 0; padding: 0; box-sizing: border-box; }
  html, body {
    width: 1200px; height: 1000px; overflow: hidden;
    background: radial-gradient(ellipse at 50% 40%, #2a2a2a 0%, var(--backdrop) 75%);
    font-family: "Roboto", Arial, sans-serif;
  }
  .card {
    position: absolute; top: 260px; width: 472px; height: 472px;
  }
  .card-back { left: 95px; background: var(--card-grey); color: var(--ink-grey); }
  .card-front { left: 624px; background: var(--brand-orange); display: flex; align-items: center; justify-content: center; }

  .name-block { position: absolute; right: 90px; top: 72px; text-align: right; }
  .name-first {
    font-weight: 300; font-size: 66px; line-height: 60px; letter-spacing: -1px;
    text-shadow: 0 1px 0 rgba(255,255,255,.35);
  }
  .name-last {
    font-weight: 700; font-size: 66px; line-height: 62px; letter-spacing: 0;
    text-shadow: 0 1px 0 rgba(255,255,255,.35);
  }
  .job-title {
    font-size: 17px; letter-spacing: 3.6px; margin-top: 10px; margin-right: -3px;
    text-shadow: 0 1px 0 rgba(255,255,255,.3);
  }
  .rule { position: absolute; left: 88px; width: 297px; height: 1px; background: var(--rule-grey); box-shadow: 0 1px 0 rgba(255,255,255,.3); }
  .rule-top { top: 258px; }
  .rule-bottom { top: 376px; }

  .contact-list { position: absolute; left: 102px; width: 280px; top: 266px; list-style: none; }
  .contact-item { display: flex; align-items: flex-start; gap: 8px; text-shadow: 0 1px 0 rgba(255,255,255,.3); }
  .contact-item svg { flex: none; width: 15px; height: 15px; margin-top: 3px; }
  .contact-email { font-size: 15px; letter-spacing: 1.1px; height: 26px; }
  .contact-web { font-size: 17px; letter-spacing: 5px; height: 30px; }
  .contact-address { font-size: 18px; line-height: 23px; }
  .address-lines { flex: 1; }
  .address-line { display: flex; justify-content: space-between; }

  .phone {
    position: absolute; left: 102px; top: 388px; display: flex; align-items: center; gap: 6px;
    font-weight: 500; font-size: 21px; letter-spacing: 3.2px; color: #8a8e94;
    text-shadow: 1px 1px 0 rgba(255,255,255,.55), -1px -1px 0 rgba(60,60,60,.45);
  }
  .phone svg { width: 20px; height: 20px; }

  .brand { display: flex; align-items: center; gap: 16px; color: var(--logo-grey); }
  .brand-mark { width: 22px; height: 22px; background: var(--logo-grey); }
  .brand-name { font-weight: 500; font-size: 58px; letter-spacing: 1px; }
</style>
</head>
<body>
  <section class="card card-back">
    <div class="name-block">
      <div class="name-first">KARIM</div>
      <div class="name-last">SALEHI</div>
      <div class="job-title">MANAGING DIRECTOR</div>
    </div>
    <div class="rule rule-top"></div>
    <ul class="contact-list">
      <li class="contact-item contact-email">
        <svg viewBox="0 0 16 16"><circle cx="8" cy="8" r="7.5" fill="#7b8087"/><rect x="4" y="5" width="8" height="6" fill="none" stroke="#c9bfba" stroke-width="1"/><path d="M4 5l4 3.2L12 5" fill="none" stroke="#c9bfba" stroke-width="1"/></svg>
        <span>karim@novlinkuae.com</span>
      </li>
      <li class="contact-item contact-web">
        <svg viewBox="0 0 16 16"><circle cx="8" cy="8" r="7.5" fill="#7b8087"/><circle cx="8" cy="8" r="4" fill="none" stroke="#c9bfba"/><path d="M4 8h8M8 4c-2 2.5-2 5.5 0 8M8 4c2 2.5 2 5.5 0 8" fill="none" stroke="#c9bfba" stroke-width=".8"/></svg>
        <span>www.novlink.ae</span>
      </li>
      <li class="contact-item contact-address">
        <svg viewBox="0 0 16 16"><circle cx="8" cy="8" r="7.5" fill="#7b8087"/><path d="M8 12.5C6 10 5 8.6 5 7a3 3 0 016 0c0 1.6-1 3-3 5.5z" fill="#c9bfba"/><circle cx="8" cy="7" r="1.1" fill="#7b8087"/></svg>
        <div class="address-lines">
          <div class="address-line"><span>Building</span><span>C2</span><span>,</span><span>Office</span><span>318</span></div>
          <div class="address-line"><span>Marsa</span><span>Tirel</span><span>Park</span></div>
        </div>
      </li>
    </ul>
    <div class="rule rule-bottom"></div>
    <div class="phone">
      <svg viewBox="0 0 20 20"><circle cx="10" cy="10" r="9" fill="#8a8e94"/><path d="M7 5.5l1.6 2.4-1 1.1c.7 1.4 1.7 2.4 3.1 3.1l1.1-1 2.4 1.6-.9 1.7c-3.6-.3-6.8-3.5-7.1-7.1z" fill="#c9bfba"/></svg>
      <span>+971 50 374 6619</span>
    </div>
  </section>

  <section class="card card-front">
    <div class="brand">
      <span class="brand-mark"></span>
      <span class="brand-name">Novlink</span>
    </div>
  </section>
</body>
</html>
```